Salon Signage

We need a new company sign designed for the exterior of our salon. I have attached our current logos for an idea. I have also attached a photo of what salon looks like currently.

```html
<!DOCTYPE html>
<html lang="en">
<head>
<meta charset="utf-8">
<title>Glosswave Beauty Salon – Exterior Signage</title>
<link href="https://fonts.googleapis.com/css2?family=Oswald:wght@300;600&family=Poppins:wght@400;500;700&display=swap" rel="stylesheet">
<style>
  :root{
    --canvas:#ffffff;
    --charcoal:#2a2527;
    --frame-line:#6a6466;
    --plum:#9b2a8f;
    --plum-deep:#7a1f71;
    --wine-dark:#1c0608;
    --wine:#5a1618;
    --white:#ffffff;
    --badge:#1f5fa8;
  }
  *{box-sizing:border-box;margin:0;padding:0}
  html,body{width:1200px;height:3058px;overflow:hidden;background:var(--canvas)}
  body{position:relative;font-family:"Poppins",sans-serif;color:var(--white)}

  .sign{position:absolute;overflow:hidden;box-shadow:0 6px 10px rgba(0,0,0,.35)}
  .sign > svg{position:absolute;inset:0;width:100%;height:100%;display:block}

  /* Fascia banner */
  .fascia{left:100px;top:1472px;width:1000px;height:300px}
  .brand{position:absolute;left:330px;top:68px;font-family:"Poppins",sans-serif;font-weight:700;color:var(--white);line-height:1}
  .brand__name{display:block;font-size:74px;letter-spacing:1px}
  .brand__sub{display:block;font-size:32px;letter-spacing:6px;margin-top:12px;padding-left:150px}
  .phone-pill{position:absolute;left:520px;top:216px;width:250px;height:52px;background:var(--white);border-radius:6px;
    display:flex;align-items:center;justify-content:center;gap:6px;color:var(--plum);font-weight:700;font-size:36px;letter-spacing:1px}
  .phone-pill svg{width:28px;height:28px}

  /* Window panels */
  .panel{top:1915px;width:470px;height:938px}
  .panel--beauty{left:100px}
  .panel--hair{left:630px}

  .panel-title{position:absolute;left:50px;top:30px;font-family:"Oswald",sans-serif;line-height:.95;color:var(--white)}
  .panel-title__light{display:block;font-weight:300;font-size:118px}
  .panel-title__bold{display:block;font-weight:600;font-size:82px;margin-top:4px}

  .service-list{position:absolute;list-style:none}
  .service-list li{display:flex;align-items:center;gap:14px;color:var(--white);font-weight:500;white-space:nowrap}
  .service-list svg{flex:none}
  .panel--beauty .service-list{left:46px;top:420px}
  .panel--beauty .service-list li{font-size:29px;height:53px}
  .panel--beauty .service-list svg{width:30px;height:26px}
  .panel--hair .service-list{left:34px;top:30px}
  .panel--hair .service-list li{font-size:34px;height:55px}
  .panel--hair .service-list svg{width:34px;height:28px}

  .panel-phone{position:absolute;display:flex;align-items:center;gap:8px;color:var(--white);letter-spacing:1px}
  .panel--beauty .panel-phone{left:40px;top:866px;font-size:34px}
  .panel--beauty .panel-phone svg{width:28px;height:28px}
  .panel--hair .panel-phone{left:0;right:0;top:856px;justify-content:center;font-size:46px;font-weight:500}
  .panel--hair .panel-phone svg{width:38px;height:38px}

  .mini-brand{position:absolute;right:26px;top:60px;font-family:"Poppins",sans-serif;font-weight:700;font-size:15px;letter-spacing:2px;color:var(--white)}
</style>
</head>
<body>

<!-- Fascia sign -->
<section class="sign fascia" aria-label="Fascia sign">
  <svg viewBox="0 0 1000 300" preserveAspectRatio="none">
    <rect width="1000" height="300" fill="var(--charcoal)"/>
    <path role="img" aria-label="Purple swirling hair texture" d="M0 0 H215 C180 110 120 190 0 212 Z" fill="var(--plum)"/>
    <path d="M0 214 C122 192 184 112 219 0" fill="none" stroke="var(--white)" stroke-width="9"/>
    <rect x="32" y="30" width="928" height="240" rx="14" fill="none" stroke="var(--frame-line)" stroke-width="2"/>
    <path role="img" aria-label="Purple swirling hair texture" d="M1000 158 C905 168 872 228 862 300 H1000 Z" fill="var(--plum)"/>
    <path d="M1000 154 C900 164 866 226 856 300" fill="none" stroke="var(--white)" stroke-width="9"/>
    <circle cx="255" cy="150" r="60" fill="none" stroke="var(--white)" stroke-width="6"/>
  </svg>
  <div class="brand">
    <span class="brand__name">GLOSSWAVE</span>
    <span class="brand__sub">BEAUTY SALON</span>
  </div>
  <div class="phone-pill">
    <svg viewBox="0 0 24 24"><path fill="currentColor" d="M6.6 10.8a15.5 15.5 0 0 0 6.6 6.6l2.2-2.2a1 1 0 0 1 1-.25 11.4 11.4 0 0 0 3.6.57 1 1 0 0 1 1 1V20a1 1 0 0 1-1 1A17 17 0 0 1 3 4a1 1 0 0 1 1-1h3.5a1 1 0 0 1 1 1c0 1.25.2 2.46.57 3.6a1 1 0 0 1-.25 1z"/></svg>
    <span>90412257</span>
  </div>
</section>

<!-- Left window panel: beauty services -->
<section class="sign panel panel--beauty" aria-label="Beauty services window panel">
  <svg viewBox="0 0 470 938" preserveAspectRatio="none">
    <defs>
      <linearGradient id="beautyPhoto" x1="0" y1="0" x2="1" y2="1">
        <stop offset="0" stop-color="#2a0709"/>
        <stop offset=".6" stop-color="#6e1a1e"/>
        <stop offset="1" stop-color="#a8403c"/>
      </linearGradient>
      <radialGradient id="portraitA" cx=".5" cy=".5" r=".6">
        <stop offset="0" stop-color="#e9c2a8"/>
        <stop offset="1" stop-color="#7a3a2c"/>
      </radialGradient>
    </defs>
    <rect role="img" aria-label="Photo of a red-haired model with dramatic makeup" width="470" height="938" fill="url(#beautyPhoto)"/>
    <path d="M0 400 C310 390 430 260 470 130 V100 H0 Z" fill="var(--white)"/>
    <path role="img" aria-label="Purple swirling hair texture" d="M0 0 H470 V100 C420 240 300 352 0 368 Z" fill="var(--plum)"/>
    <circle cx="395" cy="80" r="40" fill="var(--badge)" stroke="var(--white)" stroke-width="4"/>
    <path role="img" aria-label="Purple swirling hair texture" d="M0 812 C110 798 210 815 270 850 L470 850 V938 H0 Z" fill="var(--plum)"/>
    <path d="M0 808 C110 794 210 811 272 846" fill="none" stroke="var(--white)" stroke-width="12"/>
    <circle role="img" aria-label="Close-up photo of a model with lash extensions and red nails" cx="356" cy="846" r="86" fill="url(#portraitA)" stroke="var(--white)" stroke-width="6"/>
  </svg>
  <h2 class="panel-title">
    <span class="panel-title__light">HAIR</span>
    <span class="panel-title__bold">DRESSING</span>
  </h2>
  <ul class="service-list">
    <li><svg viewBox="0 0 30 26"><path d="M3 15 L11 22 L27 3" fill="none" stroke="currentColor" stroke-width="2.5" stroke-linecap="round" stroke-linejoin="round"/></svg>THREADING</li>
    <li><svg viewBox="0 0 30 26"><path d="M3 15 L11 22 L27 3" fill="none" stroke="currentColor" stroke-width="2.5" stroke-linecap="round" stroke-linejoin="round"/></svg>TINTING</li>
    <li><svg viewBox="0 0 30 26"><path d="M3 15 L11 22 L27 3" fill="none" stroke="currentColor" stroke-width="2.5" stroke-linecap="round" stroke-linejoin="round"/></svg>MAKEUP</li>
    <li><svg viewBox="0 0 30 26"><path d="M3 15 L11 22 L27 3" fill="none" stroke="currentColor" stroke-width="2.5" stroke-linecap="round" stroke-linejoin="round"/></svg>HAIR STYLE</li>
    <li><svg viewBox="0 0 30 26"><path d="M3 15 L11 22 L27 3" fill="none" stroke="currentColor" stroke-width="2.5" stroke-linecap="round" stroke-linejoin="round"/></svg>EYEBROW FEATHERING</li>
    <li><svg viewBox="0 0 30 26"><path d="M3 15 L11 22 L27 3" fill="none" stroke="currentColor" stroke-width="2.5" stroke-linecap="round" stroke-linejoin="round"/></svg>EYELASH EXTENSION</li>
  </ul>
  <div class="panel-phone">
    <svg viewBox="0 0 24 24"><path fill="currentColor" d="M6.6 10.8a15.5 15.5 0 0 0 6.6 6.6l2.2-2.2a1 1 0 0 1 1-.25 11.4 11.4 0 0 0 3.6.57 1 1 0 0 1 1 1V20a1 1 0 0 1-1 1A17 17 0 0 1 3 4a1 1 0 0 1 1-1h3.5a1 1 0 0 1 1 1c0 1.25.2 2.46.57 3.6a1 1 0 0 1-.25 1z"/></svg>
    <span>90412257</span>
  </div>
</section>

<!-- Right window panel: hair services -->
<section class="sign panel panel--hair" aria-label="Hair services window panel">
  <svg viewBox="0 0 470 938" preserveAspectRatio="none">
    <defs>
      <linearGradient id="hairBg" x1="0" y1="0" x2="1" y2="0">
        <stop offset="0" stop-color="var(--wine-dark)"/>
        <stop offset="1" stop-color="var(--wine)"/>
      </linearGradient>
      <linearGradient id="profilePhoto" x1="0" y1="0" x2="1" y2="1">
        <stop offset="0" stop-color="#3a0c0e"/>
        <stop offset=".5" stop-color="#8c3a2e"/>
        <stop offset="1" stop-color="#c98a6e"/>
      </linearGradient>
      <linearGradient id="modelPhoto" x1="0" y1="0" x2="0" y2="1">
        <stop offset="0" stop-color="#5fa8c8"/>
        <stop offset=".4" stop-color="#d8b49c"/>
        <stop offset="1" stop-color="#f0d2c0"/>
      </linearGradient>
      <radialGradient id="lashPhoto" cx=".5" cy=".5" r=".6">
        <stop offset="0" stop-color="#f2cdb8"/>
        <stop offset="1" stop-color="#c44d8a"/>
      </radialGradient>
      <radialGradient id="sleekPhoto" cx=".5" cy=".5" r=".6">
        <stop offset="0" stop-color="#e8d8b0"/>
        <stop offset="1" stop-color="#7a5a3a"/>
      </radialGradient>
    </defs>
    <rect width="470" height="938" fill="url(#hairBg)"/>
    <path role="img" aria-label="Photo of a model in profile with long auburn hair" d="M300 0 H470 V720 C380 640 300 560 280 420 C260 260 300 120 300 0 Z" fill="url(#profilePhoto)" opacity=".9"/>
    <rect role="img" aria-label="Photo of a model with blue pastel hair and bright makeup" x="0" y="418" width="220" height="420" fill="url(#modelPhoto)"/>
    <path role="img" aria-label="Purple swirling hair texture" d="M170 640 C260 560 380 600 470 690 V860 H170 Z" fill="var(--plum)"/>
    <circle role="img" aria-label="Close-up photo of glitter eye makeup and pink nails" cx="240" cy="500" r="62" fill="url(#lashPhoto)" stroke="var(--white)" stroke-width="5"/>
    <circle role="img" aria-label="Photo of a model with long sleek straight hair" cx="375" cy="590" r="66" fill="url(#sleekPhoto)" stroke="var(--white)" stroke-width="5"/>
    <path d="M0 860 C130 790 330 780 470 868 V938 H0 Z" fill="var(--wine-dark)"/>
    <path d="M0 860 C130 790 330 780 470 868" fill="none" stroke="var(--white)" stroke-width="10"/>
  </svg>
  <div class="mini-brand">GLOSSWAVE</div>
  <ul class="service-list">
    <li><svg viewBox="0 0 30 26"><path d="M3 15 L11 22 L27 3" fill="none" stroke="currentColor" stroke-width="2.5" stroke-linecap="round" stroke-linejoin="round"/></svg>CUT</li>
    <li><svg viewBox="0 0 30 26"><path d="M3 15 L11 22 L27 3" fill="none" stroke="currentColor" stroke-width="2.5" stroke-linecap="round" stroke-linejoin="round"/></svg>COLOUR</li>
    <li><svg viewBox="0 0 30 26"><path d="M3 15 L11 22 L27 3" fill="none" stroke="currentColor" stroke-width="2.5" stroke-linecap="round" stroke-linejoin="round"/></svg>FOILS</li>
    <li><svg viewBox="0 0 30 26"><path d="M3 15 L11 22 L27 3" fill="none" stroke="currentColor" stroke-width="2.5" stroke-linecap="round" stroke-linejoin="round"/></svg>BLOW WAVE</li>
    <li><svg viewBox="0 0 30 26"><path d="M3 15 L11 22 L27 3" fill="none" stroke="currentColor" stroke-width="2.5" stroke-linecap="round" stroke-linejoin="round"/></svg>TREATMENT</li>
    <li><svg viewBox="0 0 30 26"><path d="M3 15 L11 22 L27 3" fill="none" stroke="currentColor" stroke-width="2.5" stroke-linecap="round" stroke-linejoin="round"/></svg>STRAIGHT</li>
    <li><svg viewBox="0 0 30 26"><path d="M3 15 L11 22 L27 3" fill="none" stroke="currentColor" stroke-width="2.5" stroke-linecap="round" stroke-linejoin="round"/></svg>PERMS</li>
  </ul>
  <div class="panel-phone">
    <svg viewBox="0 0 24 24"><path fill="currentColor" d="M6.6 10.8a15.5 15.5 0 0 0 6.6 6.6l2.2-2.2a1 1 0 0 1 1-.25 11.4 11.4 0 0 0 3.6.57 1 1 0 0 1 1 1V20a1 1 0 0 1-1 1A17 17 0 0 1 3 4a1 1 0 0 1 1-1h3.5a1 1 0 0 1 1 1c0 1.25.2 2.46.57 3.6a1 1 0 0 1-.25 1z"/></svg>
    <span>90412257</span>
  </div>
</section>

</body>
</html>
```